Culture Blueprint

I would like to edit the design of this culture blueprint graphic to align with my brand colors and services graphic. Please
The ROAM stands for Leadership, Engagement, Activate Culture and Distinguish.
Work to be done:
1. Please make Purpose in red brand "roam" color
2. Please make Philosophy in grey brand "engage" color
3. Please make Priorities in and Processes (internal and external) in orange brand "active" color
4. Please make projections in teal "distinguish" color

Creativity welcomed!

```html
<!DOCTYPE html>
<html lang="en">
<head>
<meta charset="utf-8">
<title>Alignment of the Five Ps</title>
<link href="https://fonts.googleapis.com/css2?family=Arimo:wght@700&family=PT+Sans+Narrow:wght@700&family=PT+Sans:wght@400&display=swap" rel="stylesheet">
<style>
  :root {
    --roam-red: #d8262f;
    --roam-red-deep: #c11d26;
    --engage-grey: #5f5f5f;
    --engage-grey-text: #e4e4e4;
    --active-orange: #ee5b4b;
    --distinguish-teal: #0b8d99;
    --paper: #ffffff;
    --rim: #e7e7e7;
    --ink: #333333;
    --flow: rgba(70, 70, 70, 0.38);
  }
  html, body {
    margin: 0;
    padding: 0;
    width: 1144px;
    height: 1200px;
    overflow: hidden;
    background: var(--paper);
  }
  .blueprint {
    display: block;
    width: 1144px;
    height: 1200px;
  }
  .title {
    font-family: "Arimo", Arial, sans-serif;
    font-weight: 700;
    font-size: 44px;
    fill: var(--roam-red);
  }
  .band { fill: none; }
  .band--priorities { stroke: var(--engage-grey); }
  .band--inner-practices { stroke: var(--active-orange); }
  .band--outer-practices { stroke: var(--active-orange); }
  .band--projections { stroke: var(--distinguish-teal); }
  .band--rim { stroke: var(--rim); }
  .rings { filter: drop-shadow(0 3px 4px rgba(0,0,0,0.22)); }
  .philosophy-core { fill: var(--engage-grey); }
  .purpose-core { fill: var(--roam-red); }
  .purpose-banner { fill: var(--roam-red-deep); }
  .purpose-rule { stroke: var(--paper); stroke-width: 3; }
  .divider { stroke: var(--paper); stroke-linecap: butt; }
  .divider--inner, .divider--outer { stroke-width: 12; }
  .divider--projection { stroke-width: 22; }
  .flow {
    fill: none;
    stroke: var(--flow);
    stroke-width: 3;
  }
  .arrowhead { fill: var(--flow); }
  .label {
    font-family: "PT Sans Narrow", "Arial Narrow", sans-serif;
    font-weight: 700;
    fill: var(--paper);
    text-anchor: middle;
  }
  .label--core { font-size: 34px; fill: var(--engage-grey-text); letter-spacing: 1px; }
  .label--inner { font-size: 22px; }
  .label--outer { font-size: 25px; }
  .label--outer-long { font-size: 23px; }
  .label--projection { font-size: 25px; }
  .label--projection-long { font-size: 22px; }
  .label--purpose { font-size: 46px; }
  .legend-swatch--purpose { fill: var(--roam-red); }
  .legend-swatch--philosophy { fill: var(--engage-grey); }
  .legend-swatch--practices { fill: var(--active-orange); }
  .legend-swatch--projections { fill: var(--distinguish-teal); }
  .legend-text {
    font-family: "PT Sans", "Myriad Pro", sans-serif;
    font-size: 23px;
    fill: var(--ink);
  }
</style>
</head>
<body>
<svg class="blueprint" viewBox="0 0 1144 1200" xmlns="http://www.w3.org/2000/svg" role="img" aria-label="Alignment of the Five Ps culture blueprint">
  <defs>
    <!-- clockwise circles, starting at the bottom -->
    <path id="cw-90"  d="M0 90 A90 90 0 1 1 0 -90 A90 90 0 1 1 0 90"/>
    <path id="cw-154" d="M0 154 A154 154 0 1 1 0 -154 A154 154 0 1 1 0 154"/>
    <path id="cw-216" d="M0 216 A216 216 0 1 1 0 -216 A216 216 0 1 1 0 216"/>
    <path id="cw-224" d="M0 224 A224 224 0 1 1 0 -224 A224 224 0 1 1 0 224"/>
    <path id="cw-240" d="M0 240 A240 240 0 1 1 0 -240 A240 240 0 1 1 0 240"/>
    <path id="cw-321" d="M0 321 A321 321 0 1 1 0 -321 A321 321 0 1 1 0 321"/>
    <path id="cw-414" d="M0 414 A414 414 0 1 1 0 -414 A414 414 0 1 1 0 414"/>
    <path id="cw-492" d="M0 492 A492 492 0 1 1 0 -492 A492 492 0 1 1 0 492"/>
    <!-- counter-clockwise circles, starting at the top -->
    <path id="ccw-228" d="M0 -228 A228 228 0 1 0 0 228 A228 228 0 1 0 0 -228"/>
    <path id="ccw-252" d="M0 -252 A252 252 0 1 0 0 252 A252 252 0 1 0 0 -252"/>
    <path id="ccw-339" d="M0 -339 A339 339 0 1 0 0 339 A339 339 0 1 0 0 -339"/>
    <path id="ccw-432" d="M0 -432 A432 432 0 1 0 0 432 A432 432 0 1 0 0 -432"/>
    <marker id="flow-head" viewBox="0 0 10 10" refX="8" refY="5" markerWidth="5" markerHeight="5" orient="auto">
      <path class="arrowhead" d="M0 0 L10 5 L0 10 Z"/>
    </marker>
  </defs>

  <g transform="translate(572 604)">
    <text class="title"><textPath href="#cw-492" startOffset="50%" text-anchor="middle">Alignment of the Five Ps</textPath></text>

    <g class="rings">
      <circle class="band band--rim" r="380" stroke-width="10"/>
      <circle class="band band--projections" r="423" stroke-width="74"/>
      <circle class="band band--outer-practices" r="330" stroke-width="92"/>
      <circle class="band band--inner-practices" r="232" stroke-width="80"/>
      <circle class="band band--priorities" r="165" stroke-width="42"/>
      <circle class="philosophy-core" r="136"/>
    </g>

    <g class="dividers">
      <line class="divider divider--inner" x1="188" y1="0" x2="278" y2="0" transform="rotate(-120)"/>
      <line class="divider divider--inner" x1="188" y1="0" x2="278" y2="0" transform="rotate(-60)"/>
      <line class="divider divider--inner" x1="188" y1="0" x2="278" y2="0" transform="rotate(0)"/>
      <line class="divider divider--inner" x1="188" y1="0" x2="278" y2="0" transform="rotate(60)"/>
      <line class="divider divider--inner" x1="188" y1="0" x2="278" y2="0" transform="rotate(120)"/>
      <line class="divider divider--inner" x1="188" y1="0" x2="278" y2="0" transform="rotate(180)"/>

      <line class="divider divider--outer" x1="278" y1="0" x2="384" y2="0" transform="rotate(-124)"/>
      <line class="divider divider--outer" x1="278" y1="0" x2="384" y2="0" transform="rotate(-56)"/>
      <line class="divider divider--outer" x1="278" y1="0" x2="384" y2="0" transform="rotate(15)"/>
      <line class="divider divider--outer" x1="278" y1="0" x2="384" y2="0" transform="rotate(90)"/>
      <line class="divider divider--outer" x1="278" y1="0" x2="384" y2="0" transform="rotate(165)"/>

      <line class="divider divider--projection" x1="382" y1="0" x2="466" y2="0" transform="rotate(-67.5)"/>
      <line class="divider divider--projection" x1="382" y1="0" x2="466" y2="0" transform="rotate(-22.5)"/>
      <line class="divider divider--projection" x1="382" y1="0" x2="466" y2="0" transform="rotate(22.5)"/>
      <line class="divider divider--projection" x1="382" y1="0" x2="466" y2="0" transform="rotate(67.5)"/>
      <line class="divider divider--projection" x1="382" y1="0" x2="466" y2="0" transform="rotate(112.5)"/>
      <line class="divider divider--projection" x1="382" y1="0" x2="466" y2="0" transform="rotate(157.5)"/>
      <line class="divider divider--projection" x1="382" y1="0" x2="466" y2="0" transform="rotate(202.5)"/>
      <line class="divider divider--projection" x1="382" y1="0" x2="466" y2="0" transform="rotate(247.5)"/>
    </g>

    <g class="labels">
      <text class="label label--core"><textPath href="#cw-154" startOffset="50%">PRIORITIES</textPath></text>
      <text class="label label--core"><textPath href="#cw-90" startOffset="50%">PHILOSOPHY</textPath></text>

      <text class="label label--inner"><textPath href="#cw-240" startOffset="50%">STRUCTURE, WORK</textPath></text>
      <text class="label label--inner"><textPath href="#cw-216" startOffset="50%">DESIGN &amp; SYSTEMS</textPath></text>
      <text class="label label--inner"><textPath href="#cw-240" startOffset="66.7%">RECRUITMENT</textPath></text>
      <text class="label label--inner"><textPath href="#cw-216" startOffset="66.7%">&amp; SELECTION</textPath></text>
      <text class="label label--inner"><textPath href="#ccw-228" startOffset="66.7%">TRAINING &amp;</textPath></text>
      <text class="label label--inner"><textPath href="#ccw-252" startOffset="66.7%">DEVELOPMENT</textPath></text>
      <text class="label label--inner"><textPath href="#ccw-228" startOffset="50%">PERFORMANCE</textPath></text>
      <text class="label label--inner"><textPath href="#ccw-252" startOffset="50%">MANAGEMENT</textPath></text>
      <text class="label label--inner"><textPath href="#ccw-228" startOffset="33.3%">INTERNAL</textPath></text>
      <text class="label label--inner"><textPath href="#ccw-252" startOffset="33.3%">COMMUNICATIONS</textPath></text>
      <text class="label label--inner"><textPath href="#cw-224" startOffset="33.3%">TECHNOLOGY</textPath></text>

      <text class="label label--outer"><textPath href="#cw-321" startOffset="50%">CUSTOMERS</textPath></text>
      <text class="label label--outer"><textPath href="#cw-321" startOffset="69.4%">MARKETS</textPath></text>
      <text class="label label--outer"><textPath href="#ccw-339" startOffset="60.6%">PRODUCTS</textPath></text>
      <text class="label label--outer"><textPath href="#ccw-339" startOffset="39.7%">SERVICES</textPath></text>
      <text class="label label--outer-long"><textPath href="#cw-321" startOffset="30.6%">SUPPLIERS/VENDORS &amp; PARTNERS</textPath></text>

      <text class="label label--projection"><textPath href="#cw-414" startOffset="50%">NAME</textPath></text>
      <text class="label label--projection"><textPath href="#cw-414" startOffset="62.5%">LOGO/SYMBOLS</textPath></text>
      <text class="label label--projection"><textPath href="#cw-414" startOffset="75%">HEADQUARTERS</textPath></text>
      <text class="label label--projection"><textPath href="#ccw-432" startOffset="62.5%">LEADER IMAGE</textPath></text>
      <text class="label label--projection"><textPath href="#ccw-432" startOffset="50%">OFFICES/STORES</textPath></text>
      <text class="label label--projection"><textPath href="#ccw-432" startOffset="37.5%">DRESS UNIFORMS</textPath></text>
      <text class="label label--projection-long"><textPath href="#cw-414" startOffset="25%">MARKETING/PR/ADVERTISING</textPath></text>
      <text class="label label--projection-long"><textPath href="#cw-414" startOffset="37.5%">COMMUNITY ACTIVITIES</textPath></text>
    </g>

    <g class="flows">
      <path class="flow" d="M0 0 Q220 -34 440 0" marker-end="url(#flow-head)" transform="rotate(-90)"/>
      <path class="flow" d="M0 0 Q220 34 440 0" marker-end="url(#flow-head)" transform="rotate(-45)"/>
      <path class="flow" d="M0 0 Q220 -34 440 0" marker-end="url(#flow-head)" transform="rotate(0)"/>
      <path class="flow" d="M0 0 Q220 34 440 0" marker-end="url(#flow-head)" transform="rotate(45)"/>
      <path class="flow" d="M0 0 Q220 -34 440 0" marker-end="url(#flow-head)" transform="rotate(90)"/>
      <path class="flow" d="M0 0 Q220 34 440 0" marker-end="url(#flow-head)" transform="rotate(135)"/>
      <path class="flow" d="M0 0 Q220 -34 440 0" marker-end="url(#flow-head)" transform="rotate(180)"/>
      <path class="flow" d="M0 0 Q220 34 440 0" marker-end="url(#flow-head)" transform="rotate(225)"/>

      <path class="flow" d="M0 0 Q172 30 345 0" marker-end="url(#flow-head)" transform="rotate(-90)"/>
      <path class="flow" d="M0 0 Q172 -30 345 0" marker-end="url(#flow-head)" transform="rotate(-20)"/>
      <path class="flow" d="M0 0 Q172 30 345 0" marker-end="url(#flow-head)" transform="rotate(52)"/>
      <path class="flow" d="M0 0 Q172 -30 345 0" marker-end="url(#flow-head)" transform="rotate(128)"/>
      <path class="flow" d="M0 0 Q172 30 345 0" marker-end="url(#flow-head)" transform="rotate(200)"/>

      <path class="flow" d="M0 0 Q128 -24 256 0" marker-end="url(#flow-head)" transform="rotate(-30)"/>
      <path class="flow" d="M0 0 Q128 24 256 0" marker-end="url(#flow-head)" transform="rotate(30)"/>
      <path class="flow" d="M0 0 Q128 -24 256 0" marker-end="url(#flow-head)" transform="rotate(150)"/>
      <path class="flow" d="M0 0 Q128 24 256 0" marker-end="url(#flow-head)" transform="rotate(210)"/>
    </g>

    <g class="purpose">
      <circle class="purpose-core" r="76"/>
      <rect class="purpose-banner" x="-80" y="-40" width="160" height="80" rx="4"/>
      <line class="purpose-rule" x1="-72" y1="-32" x2="72" y2="-32"/>
      <line class="purpose-rule" x1="-72" y1="33" x2="72" y2="33"/>
      <text class="label label--purpose" x="0" y="17">PURPOSE</text>
    </g>
  </g>

  <g class="legend">
    <rect class="legend-swatch--purpose" x="160" y="1096" width="16" height="16"/>
    <text class="legend-text" x="197" y="1116">Purpose</text>
    <rect class="legend-swatch--philosophy" x="344" y="1096" width="16" height="16"/>
    <text class="legend-text" x="381" y="1116">Philosophy</text>
    <rect class="legend-swatch--practices" x="544" y="1096" width="16" height="16"/>
    <text class="legend-text" x="581" y="1116">Internal &amp; External</text>
    <text class="legend-text" x="581" y="1143">Practices</text>
    <rect class="legend-swatch--projections" x="834" y="1096" width="16" height="16"/>
    <text class="legend-text" x="871" y="1116">Projections</text>
  </g>
</svg>
</body>
</html>
```